Bookkeeping website design

We need a basic site design for wordpress.
We are a bookkeeping business and will need to present a look consistent with the colours and style of the logo.

Target Market(s)

Business owners

Industry/Entity Type

Accounting/Bookkeeping

Coding

Coded - Design and coding required

Number of Pages Required

1 page

```html
<!DOCTYPE html>
<html lang="en">
<head>
<meta charset="utf-8">
<title>Tally Tide Bookkeeping</title>
<link href="https://fonts.googleapis.com/css2?family=Lato:wght@400;700;900&display=swap" rel="stylesheet">
<style>
:root{
  --blue:#1bbfec;
  --green:#7cc12a;
  --ink:#1f1f1f;
  --body:#333;
  --grey-bg:#f1f1f1;
  --line:#888;
  --grad:linear-gradient(90deg,#7cc12a 0%,#1bbfec 100%);
}
*{margin:0;padding:0;box-sizing:border-box}
html,body{width:1200px;height:3170px;overflow:hidden;background:#fff}
body{font-family:'Lato',sans-serif;color:var(--body);position:relative}
.abs{position:absolute}
.btn{position:absolute;display:flex;align-items:center;justify-content:center;gap:6px;background:var(--grad);color:#fff;font-weight:900;border-radius:30px;letter-spacing:.2px}
.btn .arrow{width:14px;height:14px;border:2px solid #fff;border-radius:50%;display:flex;align-items:center;justify-content:center;font-size:9px;line-height:1}

/* header */
.site-header{position:absolute;left:0;top:0;width:1200px;height:126px;background:#fff;box-shadow:0 2px 6px rgba(0,0,0,.15);z-index:5}
.brand{position:absolute;left:75px;top:44px;display:flex;align-items:center;gap:10px;font-weight:900;font-size:24px;color:var(--ink)}
.brand .mark{width:30px;height:30px;background:var(--green)}
.nav{position:absolute;top:48px;left:445px;display:flex;gap:0;font-size:15px;font-weight:700;color:var(--ink)}
.nav a{display:block;height:33px;line-height:33px;padding:0 21px;text-decoration:none;color:var(--ink)}
.nav a.active{background:var(--blue);color:#fff;border-radius:18px;margin-right:4px}
.call{position:absolute;left:940px;top:38px}
.call .label{position:absolute;left:37px;top:2px;font-weight:700;font-size:18px;color:var(--ink);white-space:nowrap}
.call .num{position:absolute;left:37px;top:24px;font-weight:900;font-size:24px;color:var(--green);white-space:nowrap}

/* hero */
.hero{position:absolute;left:0;top:126px;width:1200px;height:704px;overflow:hidden}
.hero-photo{position:absolute;inset:0;background:linear-gradient(160deg,#d8d3c8 0%,#b9b1a4 35%,#7d7366 65%,#4c4a4c 100%)}
.hero-photo::after{content:"";position:absolute;inset:0;background:rgba(0,0,0,.18)}
.hero h1{position:absolute;left:0;width:1200px;top:208px;text-align:center;color:#fff;font-weight:900;font-size:52px;z-index:2}
.hero .sub{position:absolute;left:0;width:1200px;top:280px;text-align:center;color:#fff;font-weight:700;font-size:27px;line-height:35px;z-index:2}
.hero .btn{left:511px;top:366px;width:178px;height:53px;font-size:16px;z-index:2}
.dots{position:absolute;top:569px;left:565px;display:flex;gap:9px;z-index:2}
.dots span{width:10px;height:10px;border-radius:50%;background:#666}
.dots span:first-child{background:var(--green)}
.hero svg.wave{position:absolute;left:0;top:0;z-index:3}

/* about */
.photo-frame{position:absolute;background:#fff;padding:8px;box-shadow:0 4px 14px rgba(0,0,0,.25)}
.photo-frame .ph{width:100%;height:100%}
h2.sec{font-weight:900;color:var(--ink)}
.rule{position:absolute;width:88px;height:2px;background:var(--line)}
.about-title{position:absolute;left:616px;top:866px;font-size:33px;line-height:40px}
.about-text{position:absolute;left:616px;top:984px;width:520px;font-size:14px;line-height:28px;color:var(--body)}
.about-text p+p{margin-top:8px}

/* services */
.services{position:absolute;left:0;top:1290px;width:1200px;height:680px}
.services h2{position:absolute;top:138px;left:0;width:1200px;text-align:center;color:#fff;font-size:32px;font-weight:900}
.services .rule{background:#fff;left:556px;top:188px}
.card{position:absolute;top:228px;width:331px;height:299px;background:#fff;border-radius:6px;box-shadow:0 4px 12px rgba(0,0,0,.15);text-align:center}
.card svg{position:absolute;left:125px;top:20px}
.card h3{position:absolute;top:116px;left:0;width:100%;font-size:23px;font-weight:900;color:var(--ink)}
.card p{position:absolute;top:150px;left:18px;right:18px;font-size:13px;line-height:24px;color:var(--body)}
.card .btn{left:92px;top:239px;width:146px;height:42px;font-size:13px}
.slide-arrow{position:absolute;top:358px}

/* specialist */
.spec-title{position:absolute;left:75px;top:1988px;width:500px;font-size:33px;line-height:38px}
.spec-text{position:absolute;left:75px;top:2150px;width:520px;font-size:14.5px;line-height:24px}
.spec-text p+p{margin-top:8px}

/* contact */
.contact{position:absolute;left:0;top:2482px;width:1200px;height:313px;background:var(--grey-bg)}
.contact h2{position:absolute;top:70px;width:1200px;text-align:center;font-size:32px}
.contact .rule{left:556px;top:120px}
.ci{position:absolute;top:150px}
.ci .circle{position:absolute;left:0;top:0;width:72px;height:72px;border:2px solid #ccc;border-radius:50%;background:#fff;display:flex;align-items:center;justify-content:center}
.ci .t{position:absolute;left:87px;top:10px;white-space:nowrap;color:var(--ink)}
.ci .t b{display:block;font-size:20px;font-weight:900;margin-bottom:4px}
.ci .t span{font-size:17px;line-height:28px}

/* footer */
.footer{position:absolute;left:0;top:2795px;width:1200px;height:375px}
.footer .brand{top:82px;font-size:20px}
.footer .brand .mark{width:26px;height:26px}
.copy{position:absolute;left:75px;top:170px;font-size:13px;line-height:24px;color:var(--body)}
.social{position:absolute;left:75px;top:242px;display:flex;gap:6px}
.social span{width:29px;height:29px;border:1.5px solid var(--blue);border-radius:50%}
.fcol{position:absolute;top:72px;font-size:14px;color:var(--body)}
.fcol h4{color:var(--blue);font-size:16px;font-weight:900;margin-bottom:10px}
.fcol li{list-style:none;line-height:37.5px}
.fcol p{line-height:24px}
.fcol p+p{margin-top:4px}
</style>
</head>
<body>

<header class="site-header">
  <div class="brand"><span class="mark"></span>Tally Tide Bookkeeping</div>
  <nav class="nav">
    <a class="active" href="#">HOME</a>
    <a href="#">ABOUT US</a>
    <a href="#">SERVICES</a>
    <a href="#">CONTACT US</a>
  </nav>
  <div class="call">
    <svg width="30" height="34" viewBox="0 0 30 34"><path d="M8 6c-3 2-4 6-2 12s6 10 10 11c2 0 3-1 4-3l-4-4-3 2c-2-1-4-5-4-8l3-2-2-5z" fill="var(--green)"/><path d="M17 9a5 5 0 0 1 4 5M18 4a10 10 0 0 1 8 9" stroke="var(--green)" stroke-width="2" fill="none"/></svg>
    <div class="label">CALL US</div>
    <div class="num">0400 318 204</div>
  </div>
</header>

<section class="hero">
  <div class="hero-photo" role="img" aria-label="Photo of hands working with a calculator, notebook and pen on a desk"></div>
  <h1>Welcome to Tally Tide Bookkeeping</h1>
  <div class="sub">Not getting the balance of work/play you thought<br>you'd have as a small business owner?</div>
  <a class="btn">READ MORE <span class="arrow">›</span></a>
  <div class="dots"><span></span><span></span><span></span><span></span></div>
  <svg class="wave" width="1200" height="704" viewBox="0 0 1200 704"><path d="M0 586 C250 650 550 618 800 618 C1000 618 1120 670 1200 704 L0 704Z" fill="#fff"/></svg>
</section>

<div class="photo-frame" style="left:75px;top:850px;width:512px;height:406px">
  <div class="ph" role="img" aria-label="Photo of a desk with keyboard, calculator, glasses and a hand writing notes" style="background:linear-gradient(135deg,#e9edf0,#b7c2c9 55%,#6e7880)"></div>
</div>
<h2 class="sec about-title">About<br>Tally Tide Bookkeeping</h2>
<div class="rule" style="left:616px;top:967px"></div>
<div class="about-text">
  <p>Tally Tide Bookkeeping is an offsite bookkeeping service for small to medium business's who prefer to outsource their bookkeeping. We are located in the Northern Suburbs of Perth and service areas from Gin Gin to Joondalup.</p>
  <p>With over 30 years experience and continual ongoing education, your business will be kept up to date with the latest in legislative changes, modern awards and compliance issues.</p>
</div>
<a class="btn" style="left:616px;top:1192px;width:178px;height:54px;font-size:16px">READ MORE <span class="arrow">›</span></a>

<section class="services">
  <svg class="abs" style="left:0;top:0" width="1200" height="680" viewBox="0 0 1200 680">
    <path d="M0 6 C250 60 500 60 700 42 C900 22 1050 10 1200 105 L1200 680 L0 680Z" fill="var(--green)"/>
    <path d="M0 6 C250 60 500 62 700 56 C900 48 1050 40 1200 130 L1200 680 L0 680Z" fill="var(--blue)"/>
    <path d="M0 545 C150 600 400 640 650 620 C900 600 1050 560 1200 668 L1200 680 L0 680Z" fill="var(--green)"/>
    <path d="M0 600 C150 640 400 630 650 612 C900 592 1050 560 1200 668 L1200 680 L0 680Z" fill="#fff"/>
  </svg>
  <h2>Our Services</h2>
  <div class="rule"></div>

  <svg class="slide-arrow" style="left:40px" width="20" height="36" viewBox="0 0 20 36"><path d="M17 2 L3 18 L17 34" stroke="#fff" stroke-width="3" fill="none"/></svg>
  <svg class="slide-arrow" style="left:1142px" width="20" height="36" viewBox="0 0 20 36"><path d="M3 2 L17 18 L3 34" stroke="#fff" stroke-width="3" fill="none"/></svg>

  <div class="card" style="left:75px">
    <svg width="82" height="80" viewBox="0 0 82 80" fill="none" stroke="var(--green)" stroke-width="2.5"><rect x="6" y="30" width="44" height="40" rx="4"/><path d="M6 44h44"/><circle cx="60" cy="58" r="15" stroke="var(--blue)"/><path d="M64 51h-6a3 3 0 0 0 0 6h4a3 3 0 0 1 0 6h-7M60 47v22" stroke="var(--blue)"/><path d="M66 30V8M60 14l6-6 6 6" stroke="var(--blue)"/></svg>
    <h3>Payroll Services</h3>
    <p>Nemo enim ipsam voluptatem quia voluptas sit aspernatur aut odit aut fugit, sed quia co nsequuntur magni dolores .</p>
    <a class="btn">READ MORE <span class="arrow">›</span></a>
  </div>
  <div class="card" style="left:437px">
    <svg width="82" height="80" viewBox="0 0 82 80" fill="none" stroke-width="2.5"><path d="M6 40 L22 24 L40 32 L58 24 L76 40 L50 64 L32 48" stroke="var(--green)"/><path d="M22 46 L40 64 M30 40 L48 58" stroke="var(--blue)"/><path d="M41 4v10M24 8l5 8M58 8l-5 8" stroke="var(--blue)"/></svg>
    <h3>Bank Reconciliation</h3>
    <p>Nemo enim ipsam voluptatem quia voluptas sit aspernatur aut odit aut fugit, sed quia co nsequuntur magni dolores .</p>
    <a class="btn">READ MORE <span class="arrow">›</span></a>
  </div>
  <div class="card" style="left:796px">
    <svg width="82" height="80" viewBox="0 0 82 80" fill="none" stroke-width="2.5"><rect x="14" y="4" width="54" height="72" rx="4" stroke="var(--green)"/><rect x="22" y="14" width="38" height="22" stroke="var(--blue)"/><path d="M28 32v-8M36 32v-12M44 32v-6M52 32v-14" stroke="var(--green)"/><circle cx="32" cy="54" r="9" stroke="var(--blue)"/><path d="M32 45v9h9M46 50h14M46 56h14M46 62h14" stroke="var(--green)"/></svg>
    <h3>Financial Reporting</h3>
    <p>Nemo enim ipsam voluptatem quia voluptas sit aspernatur aut odit aut fugit, sed quia co nsequuntur magni dolores .</p>
    <a class="btn">READ MORE <span class="arrow">›</span></a>
  </div>
</section>

<h2 class="sec spec-title">LedgerPro Specialist | Registered BAS Agent | Bookkeeper for Small Business</h2>
<div class="rule" style="left:75px;top:2124px"></div>
<div class="spec-text">
  <p>Hate doing your BAS? Is it overdue again? Our bookkeepers can help you sort it all out and more! Call us today.</p>
  <p>We are registered BAS service providers who love to help small and medium businesses maintain their financial records and do their BAS.<br>Need an in-house bookkeeper – but not full time?</p>
  <p>Streamline your bookkeeping with our reliable, seamless and professional service.</p>
</div>
<a class="btn" style="left:75px;top:2348px;width:178px;height:54px;font-size:16px">READ MORE <span class="arrow">›</span></a>
<div class="photo-frame" style="left:615px;top:1995px;width:512px;height:407px">
  <div class="ph" role="img" aria-label="Photo of a smiling bookkeeper seated beside a computer screen in an office" style="background:linear-gradient(120deg,#cfd3d6,#eceae6 50%,#d9b7b4 80%,#c39d97)"></div>
</div>

<section class="contact">
  <h2 class="sec">Contact Address</h2>
  <div class="rule"></div>
  <div class="ci" style="left:75px">
    <div class="circle"><svg width="28" height="36" viewBox="0 0 28 36"><path d="M14 0a13 13 0 0 0-13 13c0 10 13 23 13 23s13-13 13-23A13 13 0 0 0 14 0z" fill="var(--green)"/><circle cx="14" cy="13" r="5" fill="#fff"/></svg></div>
    <div class="t"><b>Address:</b><span>Coral Point,<br>Western Australia 6000</span></div>
  </div>
  <div class="ci" style="left:472px">
    <div class="circle"><svg width="34" height="34" viewBox="0 0 30 34"><path d="M8 6c-3 2-4 6-2 12s6 10 10 11c2 0 3-1 4-3l-4-4-3 2c-2-1-4-5-4-8l3-2-2-5z" fill="var(--green)"/><path d="M17 9a5 5 0 0 1 4 5M18 4a10 10 0 0 1 8 9" stroke="var(--green)" stroke-width="2" fill="none"/></svg></div>
    <div class="t" style="top:12px"><b>Phone:</b><span style="font-size:20px">0400 318 204</span></div>
  </div>
  <div class="ci" style="left:772px">
    <div class="circle"><svg width="36" height="26" viewBox="0 0 36 26"><rect width="36" height="26" rx="2" fill="var(--green)"/><path d="M2 3l16 12L34 3" stroke="#fff" stroke-width="2.5" fill="none"/></svg></div>
    <div class="t" style="top:12px"><b>Email:</b><span>jordan@tallytide.com.au</span></div>
  </div>
</section>

<footer class="footer">
  <div class="brand"><span class="mark"></span>Tally Tide Bookkeeping</div>
  <div class="copy">&nbsp;© 2021 Tally Tide Bookkeeping.<br>All Rights Reserved</div>
  <div class="social"><span></span><span></span><span></span><span></span><span></span></div>
  <div class="fcol" style="left:342px;width:250px">
    <h4>ABOUT US</h4>
    <p>Tally Tide Bookkeeping is a small bookkeeping business run by Jordan Ellery.</p>
    <p>Jordan is a professional bookkeeper and BAS Agent with over 30 years experience.</p>
  </div>
  <div class="fcol" style="left:651px">
    <h4>QUICK MENU</h4>
    <ul><li>Home</li><li>About Us</li><li>Our Services</li><li>Contact Us</li></ul>
  </div>
  <div class="fcol" style="left:885px">
    <h4>OUR SERVICES</h4>
    <ul><li>BAS/IAS</li><li>Payroll Services</li><li>Bank Reconciliation</li><li>AC's Payable/Receivable</li><li>State Revenue PRT</li><li>Financial Reporting</li></ul>
  </div>
</footer>

</body>
</html>
```